Design some Business Cards

We are a Photography and Social Media company that takes pictures for business and individuals and creates Lumigrove, Glimmerdot, Quillo etc. We need a very creative business card that has our logo. We will be getting our business cards from kestrel ink. We don't have a set location yet so the address can be 478 fernwood lane Brooklyn NY 11987. phone number xxx-xxx-xxxx

Please find our logo attached.

Please incorporate both logos.

Please have both logos on separate sides of the business card.

```html
<!DOCTYPE html>
<html lang="en">
<head>
<meta charset="utf-8">
<title>Fennick Studio – Business Cards</title>
<link href="https://fonts.googleapis.com/css2?family=Arimo:wght@400&display=swap" rel="stylesheet">
<style>
  :root {
    --bg: #ecebe8;
    --card: #ffffff;
    --ink: #1c1c1c;
    --logo-ink: #333333;
    --band-dark: #111111;
    --band-light: #9a9a9a;
    --texture: #4a4a4a;
    --band-text: #f2f2f2;
  }
  * { box-sizing: border-box; margin: 0; padding: 0; }
  html, body { width: 1200px; height: 1200px; overflow: hidden; }
  body {
    background: var(--bg);
    display: flex;
    flex-direction: column;
    align-items: center;
    justify-content: center;
    gap: 60px;
    font-family: "Arimo", sans-serif;
  }
  .card {
    position: relative;
    width: 860px;
    height: 491px;
    background: var(--card);
    box-shadow: 0 6px 18px rgba(0,0,0,0.12);
    overflow: hidden;
  }

  /* business name set as plain text with one square marker */
  .wordmark {
    font-family: "Arimo", sans-serif;
    font-weight: 400;
    color: var(--logo-ink);
    display: flex;
    align-items: center;
    white-space: nowrap;
  }
  .wordmark-square {
    background: var(--logo-ink);
    flex: none;
  }

  /* contact side */
  .card-contact .wordmark {
    position: absolute;
    left: 70px; top: 156px;
    font-size: 32px;
    gap: 14px;
  }
  .card-contact .wordmark-square { width: 14px; height: 14px; }
  .divider {
    position: absolute;
    left: 420px; top: 112px;
    width: 5px; height: 130px;
    background: var(--ink);
  }
  .contact-list {
    position: absolute;
    left: 450px; top: 110px;
    list-style: none;
    font-size: 23px;
    color: var(--ink);
    line-height: 1.35;
  }
  .contact-list li { display: flex; align-items: flex-start; gap: 14px; }
  .contact-list svg { width: 20px; height: 20px; margin-top: 4px; flex: none; }
  .contact-list .address { flex-direction: column; gap: 0; padding-left: 34px; position: relative; }
  .contact-list .address svg { position: absolute; left: 0; top: 0; }

  .band {
    position: absolute;
    left: 0; right: 0;
    background: linear-gradient(90deg, var(--band-dark) 0%, var(--band-dark) 35%, var(--band-light) 60%, var(--band-dark) 85%, var(--band-dark) 100%);
  }
  .card-contact .band { bottom: 0; height: 34px; }
  .band-texture {
    position: absolute;
    top: 0; bottom: 0;
    background: linear-gradient(90deg, transparent, var(--texture), transparent);
  }
  .card-contact .band-texture { left: 180px; width: 120px; }

  /* logo side */
  .card-logo .wordmark {
    position: absolute;
    left: 0; right: 0; top: 150px;
    justify-content: center;
    font-size: 64px;
    gap: 24px;
  }
  .card-logo .wordmark-square { width: 26px; height: 26px; }
  .card-logo .band { bottom: 44px; height: 56px; }
  .card-logo .band-texture { left: 60px; width: 130px; }
  .band-url {
    position: absolute;
    left: 200px; top: 50%;
    transform: translateY(-50%);
    font-size: 20px;
    letter-spacing: 5px;
    color: var(--band-text);
  }
</style>
</head>
<body>

  <section class="card card-contact" aria-label="Business card contact side">
    <div class="wordmark">
      <span class="wordmark-square"></span>
      <span class="wordmark-name">Fennick Studio</span>
    </div>
    <div class="divider"></div>
    <ul class="contact-list">
      <li>
        <svg viewBox="0 0 20 20" aria-hidden="true"><path d="M4 2l4 1 1 4-2 1.5a11 11 0 0 0 4.5 4.5L13 11l4 1 1 4-2 2C9 18 2 11 2 4z" fill="var(--ink)"/></svg>
        <span>+123-XXXXX</span>
      </li>
      <li>
        <svg viewBox="0 0 20 20" aria-hidden="true"><rect x="2" y="4" width="16" height="12" fill="none" stroke="var(--ink)" stroke-width="1.8"/><path d="M2 4l8 7 8-7" fill="none" stroke="var(--ink)" stroke-width="1.8"/></svg>
        <span>jon@fennickstudio.com</span>
      </li>
      <li>
        <svg viewBox="0 0 20 20" aria-hidden="true"><circle cx="10" cy="10" r="8" fill="none" stroke="var(--ink)" stroke-width="1.8"/><ellipse cx="10" cy="10" rx="3.5" ry="8" fill="none" stroke="var(--ink)" stroke-width="1.5"/><path d="M2 10h16" stroke="var(--ink)" stroke-width="1.5"/></svg>
        <span>www.fennickstudio.com</span>
      </li>
      <li class="address">
        <svg viewBox="0 0 20 20" aria-hidden="true"><path d="M10 19s-6-6.5-6-11a6 6 0 0 1 12 0c0 4.5-6 11-6 11z" fill="none" stroke="var(--ink)" stroke-width="1.8"/><circle cx="10" cy="8" r="2.2" fill="var(--ink)"/></svg>
        <span>478 fernwood lane</span>
        <span>Booklyn NY 11987</span>
      </li>
    </ul>
    <div class="band">
      <div class="band-texture" role="img" aria-label="Grunge speckle texture on the band"></div>
    </div>
  </section>

  <section class="card card-logo" aria-label="Business card logo side">
    <div class="wordmark">
      <span class="wordmark-square"></span>
      <span class="wordmark-name">Fennick Studio</span>
    </div>
    <div class="band">
      <div class="band-texture" role="img" aria-label="Grunge speckle texture on the band"></div>
      <span class="band-url">www.fennickstudio.com</span>
    </div>
  </section>

</body>
</html>
```